Homepage design for site providing cloud based engineering applications

I need the design for the homepage of a new site providing cloud based engineering applicaitons. The items that must have are provided in the attached pdf file. The layout and colors shown in the attached file is not intened to restrict your design. You should be creative to come up with your best design. We may have many applications. How to show these applicaitons on the homepage would be very important. Anyway, we want our hompage to be simple and clear.

Target Market(s)

Structure engineers(People design bridges, buildings and wharfs etc.)

Industry/Entity Type

Engineering

Requirements
Must have
• See attached pdf file.
Should not have
• No flash will be used.

```html
<!DOCTYPE html>
<html lang="en">
<head>
<meta charset="utf-8">
<title>Best Engineering Applications</title>
<link href="https://fonts.googleapis.com/css2?family=Ubuntu:ital,wght@0,300;0,400;0,500;1,400;1,500&display=swap" rel="stylesheet">
<style>
:root{
  --bg:#e6eaed;
  --bg-light:#f1f3f5;
  --blue:#1b9be6;
  --blue-dark:#1a5fc2;
  --navy:#1c2a3b;
  --text:#7b8188;
  --heading:#2a2f35;
  --muted:#a8aeb4;
  --footer:#2b3033;
  --footer-low:#272b2e;
  --footer-text:#9aa0a5;
  --white:#ffffff;
}
*{margin:0;padding:0;box-sizing:border-box}
html,body{width:1180px;height:1200px;overflow:hidden}
body{font-family:"Ubuntu",sans-serif;background:var(--bg);position:relative;color:var(--text)}
.page-top{position:absolute;left:0;top:0;width:1180px;height:815px;
  background:radial-gradient(ellipse at 85% 15%,#f7f8f9 0%,var(--bg-light) 30%,var(--bg) 70%)}
.abs{position:absolute}

.logo{left:168px;top:32px;width:100px;height:100px;border-radius:50%;background:var(--blue);
  display:flex;align-items:center;justify-content:center;text-align:center;
  color:var(--white);font-weight:500;font-size:32px;line-height:30px;letter-spacing:-1px}

.social{display:flex;gap:4px}
.social span{width:22px;height:22px;border-radius:3px;display:block}
.social .fb{background:#3b5b9a}
.social .tw{background:#4fc1ee}

.main-nav{left:374px;top:61px;height:43px;display:flex;background:var(--white);
  box-shadow:0 1px 3px rgba(0,0,0,.15)}
.main-nav a{display:flex;align-items:center;justify-content:center;width:100px;height:43px;
  font-size:12.5px;color:#2b2f33;text-decoration:none;border-left:1px solid #e3e5e7}
.main-nav a.home{width:46px;border-left:none;background:#f4f5f6}
.main-nav a.active{color:var(--blue)}
.main-nav a.login{width:108px;background:var(--navy);color:var(--white);gap:7px;border-left:none}

.rule{height:1px;background:#d2d7db}
.tagline{left:0;width:1204px;top:178px;text-align:center;font-weight:300;font-size:29px;color:var(--muted);letter-spacing:.5px}

.hero-media{left:163px;top:268px;width:454px;height:395px;border-radius:10px;
  background:linear-gradient(150deg,#1e2224 0%,#2a6f78 30%,#5cc3c5 55%,#1b3f47 85%,#c8ccd0 100%)}
.card-fold{left:577px;top:312px;width:67px;height:31px;background:linear-gradient(#b8c0cc,#8c96a4);clip-path:polygon(0 100%,100% 0,100% 100%)}
.app-card{left:577px;top:343px;width:449px;height:145px;background:var(--white);padding:14px 17px}
.app-card h1{font-weight:400;font-size:27px;color:var(--heading);letter-spacing:.5px;padding-bottom:9px;border-bottom:1px solid #e1e3e5;width:411px}
.app-card p{font-size:11.3px;line-height:18px;margin-top:13px;color:#8a8f94}
.app-card p a{color:var(--blue);text-decoration:none}
.price{left:903px;top:286px;width:82px;height:82px;border-radius:50%;background:var(--blue);color:var(--white);
  text-align:center;padding-top:13px;font-size:19px;line-height:23px}
.price strong{font-weight:400;font-size:24px;display:block}

.actions{left:677px;top:488px;display:flex;gap:9px}
.actions a{width:79px;height:66px;background:var(--blue);color:var(--white);text-decoration:none;
  font-size:12px;display:flex;flex-direction:column;align-items:center;justify-content:flex-end;padding-bottom:10px;gap:10px}

.pager{width:70px;height:70px;border-radius:50%;background:#bfc4c8;display:flex;align-items:center;justify-content:center}
.pager-label{font-size:18px;color:#b3b8bd;width:70px;text-align:center}

.thumbs{left:162px;top:690px;width:860px;height:96px}
.thumb{position:absolute;top:0;width:94px;height:96px;border:2px solid #d4d8db;border-radius:2px}
.thumb-selected{left:263px;top:681px;width:110px;height:112px;background:var(--blue-dark)}
.thumb-selected::before{content:"";position:absolute;left:34px;top:-10px;border-left:21px solid transparent;border-right:21px solid transparent;border-bottom:10px solid var(--blue-dark)}
.thumb-selected .thumb-img{position:absolute;left:10px;top:12px;width:90px;height:90px;background:linear-gradient(140deg,#2c4e52,#5bb7b5 50%,#2a3a3e)}

.site-footer{left:0;top:815px;width:1180px;height:385px;background:var(--footer)}
.footer-low{left:0;top:1069px;width:1180px;height:131px;background:var(--footer-low)}
.footer-col h2{font-weight:400;font-size:24px;color:#e8eaec;letter-spacing:.3px}
.footer-col p{font-size:11.5px;line-height:18.2px;color:var(--footer-text);margin-top:24px}
.tweet{left:573px;top:893px;width:204px;height:104px;background:#26292c;padding:7px 8px}
.tweet p{margin-top:0}
.tweet .handle{color:var(--blue)}
.tweet em{font-size:10.5px;color:#d6d8da}
.tweet::after{content:"";position:absolute;left:128px;bottom:-9px;border-left:10px solid transparent;border-right:10px solid transparent;border-top:9px solid #26292c}
.bird{left:722px;top:1008px;width:30px;height:30px;border-radius:50%;background:var(--blue)}
.author{font-style:italic;font-weight:500;font-size:11.5px;color:#c8ccd0}

.legal{left:161px;top:1091px;font-size:11.5px;color:var(--footer-text)}
.legal a{color:var(--footer-text);text-decoration:none}
.legal .sep{margin:0 6px}
.copyright{left:720px;top:1091px;width:297px;text-align:right;font-size:11.5px;color:#3e4448}
.bottom-rule{left:162px;top:1126px;width:856px;height:1px;background:#3a4044}
</style>
</head>
<body>
<div class="page-top"></div>

<header>
  <div class="abs logo">YOUR<br>LOGO</div>
  <div class="abs social" style="left:972px;top:24px"><span class="fb"></span><span class="tw"></span></div>
  <nav class="abs main-nav">
    <a class="home" href="#"><svg width="14" height="12" viewBox="0 0 14 12"><path d="M7 0L0 6h2v6h4V8h2v4h4V6h2z" fill="#9aa0a6"/></svg></a>
    <a href="#">PRODUCTS</a>
    <a class="active" href="#">BUY NOW</a>
    <a href="#">SUPPORT</a>
    <a href="#">ABOUT US</a>
    <a href="#">CONTACT</a>
    <a class="login" href="#"><svg width="15" height="16" viewBox="0 0 15 16"><circle cx="7.5" cy="4" r="4" fill="#fff"/><path d="M0 16c0-5 3-7 7.5-7S15 11 15 16z" fill="#fff"/></svg>USER LOGIN</a>
  </nav>
</header>

<div class="abs rule" style="left:0;top:170px;width:615px"></div>
<div class="abs tagline">best engineering applicaitons</div>
<div class="abs rule" style="left:168px;top:223px;width:1012px"></div>

<section class="hero">
  <div class="abs pager" style="left:30px;top:397px"><svg width="20" height="40" viewBox="0 0 20 40"><path d="M18 2L3 20l15 18" fill="none" stroke="#fff" stroke-width="2"/></svg></div>
  <div class="abs pager-label" style="left:30px;top:470px">prev</div>
  <div class="abs pager" style="left:1071px;top:397px"><svg width="20" height="40" viewBox="0 0 20 40"><path d="M2 2l15 18L2 38" fill="none" stroke="#fff" stroke-width="2"/></svg></div>
  <div class="abs pager-label" style="left:1071px;top:470px">next</div>

  <div class="abs hero-media" role="img" aria-label="Desktop monitor showing an engineering application screen with a machine control panel"></div>
  <div class="abs card-fold"></div>
  <div class="abs app-card">
    <h1>Application name</h1>
    <p>Lorem ipsum dolor sit amet, consectetur adipiscing elit. Sed lobortis varius justo ac pulvinar. Maecenas lobortis eleifend augue, eget. Lorem ipsum dolor sit amet, consectetur adipiscing elit. Sed ... <a href="#">More details &gt;</a></p>
  </div>
  <div class="abs price">only<strong>$9,99</strong></div>

  <div class="abs actions">
    <a href="#"><svg width="16" height="18" viewBox="0 0 16 18"><path d="M1 0l15 9-15 9z" fill="#fff"/></svg>Free Trial</a>
    <a href="#"><svg width="24" height="20" viewBox="0 0 24 20"><path d="M0 1h4l3 11h13l3-8H6" fill="none" stroke="#fff" stroke-width="2.4"/><circle cx="9" cy="17" r="2" fill="#fff"/><circle cx="18" cy="17" r="2" fill="#fff"/></svg>Buy it Now</a>
    <a href="#"><svg width="22" height="20" viewBox="0 0 22 20"><rect x="1" y="1" width="20" height="18" fill="none" stroke="#fff" stroke-width="2"/><path d="M4 16l5-6 4 4 3-3 3 5z" fill="#fff"/><circle cx="15" cy="6" r="2" fill="#fff"/></svg>ScreenShots</a>
    <a href="#"><svg width="22" height="22" viewBox="0 0 22 22"><path d="M18 11a7 7 0 1 1-3-5.7" fill="none" stroke="#fff" stroke-width="3.2"/><path d="M12 1l8 3-6 6z" fill="#fff"/></svg>Lunch App</a>
  </div>
</section>

<section class="abs thumbs">
  <div class="thumb" role="img" aria-label="Calculator keypad" style="left:0;background:linear-gradient(135deg,#c94b4b,#3d8fc4 50%,#e8e8e8)"></div>
  <div class="thumb" role="img" aria-label="Flow unit table" style="left:218px;background:linear-gradient(90deg,#e9ebee 60%,#9aa2b4 60%)"></div>
  <div class="thumb" role="img" aria-label="Star to delta conversion screen" style="left:327px;background:linear-gradient(180deg,#e07b1e,#c85c10)"></div>
  <div class="thumb" role="img" aria-label="Engine rendering" style="left:436px;background:linear-gradient(135deg,#dfe3e8,#3d5f9a 55%,#6d6f73)"></div>
  <div class="thumb" role="img" aria-label="Flow unit table" style="left:545px;background:linear-gradient(90deg,#e9ebee 60%,#9aa2b4 60%)"></div>
  <div class="thumb" role="img" aria-label="Star to delta conversion screen" style="left:653px;background:linear-gradient(180deg,#e07b1e,#c85c10)"></div>
  <div class="thumb" role="img" aria-label="Engine rendering" style="left:762px;background:linear-gradient(135deg,#dfe3e8,#3d5f9a 55%,#6d6f73)"></div>
</section>
<div class="abs thumb-selected"><div class="thumb-img" role="img" aria-label="Machine control panel application"></div></div>

<footer>
  <div class="abs site-footer"></div>
  <div class="abs footer-low"></div>

  <div class="abs footer-col" style="left:163px;top:846px;width:375px">
    <h2>About us ...</h2>
    <p>Lorem ipsum dolor sit amet, consectetur adipiscing elit. Sed lobortis varius justo ac pulvinar. Maecenas lobortis eleifend augue, eget. Lorem ipsum dolor sit amet, consectetur adipiscing ulvinar. Maecenas lobortis eleifend augue, eget. Lorem ipsum dolor sit amet, consectetur adipi-scing elit. Sed lobortis varius justo ac pulvinar. Maecenas lobortis eleifend augue, eget</p>
  </div>

  <div class="abs footer-col" style="left:581px;top:846px">
    <h2>Chirper updates</h2>
  </div>
  <div class="abs footer-col tweet">
    <p><span class="handle">@ Lorem ipsum</span> dolor sit amet, con-sectetur adipiscing elit. Sed lobortis varius justo ac pulvinar. Maecenas lobortis eleifend augue,<br><em>2 minutes ago via PostDeck</em></p>
  </div>
  <div class="abs bird"></div>

  <div class="abs footer-col" style="left:816px;top:846px;width:200px">
    <h2>Testimonies</h2>
    <p>“ Lorem ipsum dolor sit amet, con-sectetur adipiscing elit. Sed lobortis varius justo ac pulvinar. Maecenas lobortis eleifend augue, eget. Lorem ipsum dolor sit amet, consectetur adipiscing elit. ”</p>
    <p class="author" style="margin-top:20px">Mr John John</p>
  </div>

  <nav class="abs legal">
    <a href="#">Log in</a><span class="sep">|</span><a href="#">Privacy Policy</a><span class="sep">|</span><a href="#">Terms and Conditions</a><span class="sep">|</span><a href="#">Contact Us</a><span class="sep">|</span><a href="#">Back to Top</a>
  </nav>
  <div class="abs social" style="left:642px;top:1086px"><span class="fb"></span><span class="tw"></span></div>
  <div class="abs copyright">© 2011 Copyright your name. All Rights Reserved</div>
  <div class="abs bottom-rule"></div>
</footer>
</body>
</html>
```